5th Battalion 42nd Cavalry Regiment " Grey Falcons"

Hello,
I am a lieutenant in the Northmark Defense Corps and my boss lieutenant colonel (commander) has asked me to come up with a business card for him. I threw a few designs toward him and he declined all of them. He really like the Knight business card background that is attached below(, but would like another Knight to replace it). We are 5th Battalion 42nd Cavalry Regiment (Grey Falcons is are Battalion Symbol) and are a Heavy Armored Combat team( Tanks and Carver's). He is an Infantry LTC would love a Bold but simple Grey Falcon riding on a horse. It doesn’t have to have the same back ground as the attached file named Finished Card, but will need all the information that is on both sides of the card. Thank you very much for your help and I look forward to seeing the designs.
V/R
Dale Whitcombe

Reason: My boss would like to see a few more designs.

```html
<!DOCTYPE html>
<html lang="en">
<head>
<meta charset="utf-8">
<title>Grey Falcons Battalion Commander Card</title>
<link rel="stylesheet" href="https://fonts.googleapis.com/css2?family=Tinos:wght@400;700&display=swap">
<style>
  :root {
    --page-bg: #d9d9d9;
    --card-dark: #363636;
    --card-edge: #1f1f1f;
    --band-grey: #a9a9a9;
    --band-text: #2a2a2a;
    --ink-light: #f2f2f2;
    --card-light: #efefef;
    --ink-dark: #1c1c1c;
    --strip-dark: #262626;
  }
  * { margin: 0; padding: 0; box-sizing: border-box; }
  html, body { width: 1200px; height: 960px; overflow: hidden; }
  body {
    background: var(--page-bg);
    font-family: "Tinos", "Times New Roman", serif;
    position: relative;
  }
  .card {
    position: absolute;
    left: 200px;
    width: 800px;
    height: 440px;
    border-radius: 18px;
    overflow: hidden;
    box-shadow: 0 10px 24px rgba(0,0,0,0.25);
  }
  /* Front */
  .card-front {
    top: 20px;
    background: var(--card-dark);
    border: 6px solid var(--card-edge);
  }
  .front-header {
    position: absolute;
    top: 10px; left: 230px; right: 10px;
    height: 40px;
    background: var(--band-grey);
    color: var(--band-text);
    font-size: 30px;
    line-height: 40px;
    text-align: right;
    padding-right: 18px;
  }
  .front-art {
    position: absolute;
    top: 50px; right: 10px;
    width: 410px; bottom: 50px;
    background: radial-gradient(ellipse at 65% 35%, #a9a394 0%, #5e5a4e 40%, #2a2a24 85%);
  }
  .front-contact {
    position: absolute;
    top: 70px; left: 36px;
    color: var(--ink-light);
    font-size: 19px;
    line-height: 23px;
  }
  .front-contact .address { margin-bottom: 18px; }
  .front-footer {
    position: absolute;
    bottom: 10px; left: 10px;
    width: 630px;
    height: 40px;
    background: var(--band-grey);
    color: var(--band-text);
    font-size: 30px;
    line-height: 40px;
    padding-left: 18px;
  }
  /* Back */
  .card-back {
    top: 500px;
    background: var(--card-light);
  }
  .back-art {
    position: absolute;
    inset: 0 0 78px 0;
    background: radial-gradient(ellipse at 50% 55%, #cfcfcf 0%, #e2e2e2 45%, #f1f1f1 80%);
  }
  .vision {
    position: absolute;
    top: 80px; left: 0; right: 0;
    text-align: center;
    color: var(--ink-dark);
  }
  .vision-title {
    font-size: 24px;
    font-weight: 700;
    letter-spacing: 0.5px;
    margin-bottom: 8px;
  }
  .vision-text {
    font-size: 24px;
    line-height: 29px;
  }
  .back-strip {
    position: absolute;
    left: 0; right: 0; bottom: 14px;
    height: 64px;
    background: var(--strip-dark);
    color: var(--ink-light);
    font-size: 26px;
    display: flex;
    justify-content: space-between;
    align-items: center;
    padding: 0 30px;
  }
</style>
</head>
<body>
  <section class="card card-front">
    <div class="front-header">5th Battalion, 42nd Cavalry Regiment</div>
    <div class="front-art" role="img" aria-label="Mounted knight on horseback before a dark castle wall"></div>
    <div class="front-contact">
      <p class="address">2261 Harlow St.<br>Camp Redmont, ND 58107</p>
      <p>Work: 555-240-0138<br>BB: 555-250-0194<br>Cell: 555-720-0167<br>Email: marcus.r.halvorsen.mil@mail.mil</p>
    </div>
    <div class="front-footer">Battalion Commander, MARCUS HALVORSEN</div>
  </section>

  <section class="card card-back">
    <div class="back-art" role="img" aria-label="Faded mounted knights before a castle, used as a light background"></div>
    <div class="vision">
      <h2 class="vision-title">GREY FALCON UNIT VISION</h2>
      <p class="vision-text">A superbly fit, trained, disciplined, ready, and adaptable unit,<br>excercising mission command and<br>teamwork to aggressively execute<br>any mission and win!</p>
    </div>
    <div class="back-strip">
      <span>Always towards the enemy</span>
      <span>Strike First</span>
    </div>
  </section>
</body>
</html>
```